Wageline Associates Business Card Design

We need a business card designed around our new logo. The business card should be modern in design & should communicate success, confidence, power, sophistication. The target market is young business professionals. This is for a human resource & payroll outsourcing business.

```html
<!DOCTYPE html>
<html lang="en">
<head>
<meta charset="utf-8">
<title>Wageline Associates Business Card</title>
<link href="https://fonts.googleapis.com/css2?family=Roboto:wght@400;500;700&display=swap" rel="stylesheet">
<style>
  :root {
    --stage: #8a8a8a;
    --card-white: #ffffff;
    --card-black: #050505;
    --brand-red: #e3121b;
    --ink: #1a1a1a;
    --muted: #6b6b6b;
    --text-light: #f2f2f2;
  }
  * { box-sizing: border-box; margin: 0; padding: 0; }
  html, body {
    width: 1200px; height: 900px; overflow: hidden;
    background: var(--stage);
    font-family: "Roboto", Arial, sans-serif;
  }
  .stage {
    position: relative; width: 1200px; height: 900px;
    display: flex; align-items: center; justify-content: center; gap: 40px;
  }
  .card {
    position: relative; width: 525px; height: 300px; overflow: hidden;
    box-shadow: 0 10px 30px rgba(0,0,0,0.35);
  }
  .card--front { background: var(--card-white); }
  .card--back { background: var(--card-black); }
  .front-sweep { position: absolute; inset: 0; width: 100%; height: 100%; }

  .wordmark { display: flex; align-items: center; gap: 8px; }
  .wordmark__dot {
    width: 12px; height: 12px; border-radius: 50%;
    background: var(--brand-red); flex: none;
  }
  .wordmark__name {
    font-weight: 500; font-size: 25px; line-height: 1.1; letter-spacing: 0.2px;
  }
  .card--front .wordmark { position: absolute; left: 30px; top: 52px; width: 200px; }
  .card--front .wordmark__name { color: var(--ink); }

  .divider {
    position: absolute; left: 245px; top: 40px; width: 2px; height: 130px;
    background: var(--brand-red);
  }
  .holder { position: absolute; left: 262px; top: 44px; }
  .holder__name {
    color: var(--brand-red); font-weight: 700; font-size: 24px;
    letter-spacing: 0.5px; text-transform: uppercase; line-height: 1.15;
  }
  .holder__role {
    color: var(--muted); font-size: 11px; letter-spacing: 0.4px;
    text-transform: uppercase; margin-top: 2px;
  }
  .holder__address {
    color: var(--muted); font-size: 14px; line-height: 1.35; margin-top: 6px;
    font-style: normal;
  }
  .contact-list {
    list-style: none; position: absolute; left: 262px; top: 150px;
    color: var(--muted); font-size: 14px; line-height: 1.6;
  }
  .contact-list li { display: flex; align-items: center; gap: 7px; }
  .contact-list svg { width: 12px; height: 12px; flex: none; }

  .card--back .wordmark {
    position: absolute; left: 0; right: 0; top: 108px; justify-content: center;
  }
  .card--back .wordmark__name { color: var(--text-light); font-size: 32px; }
  .back-url {
    position: absolute; left: 0; right: 0; top: 222px; text-align: center;
    color: var(--text-light); font-size: 13px; letter-spacing: 0.3px;
  }
</style>
</head>
<body>
<main class="stage">
  <section class="card card--front" aria-label="Business card front">
    <svg class="front-sweep" viewBox="0 0 525 300" preserveAspectRatio="none" aria-hidden="true">
      <path d="M0,255 Q170,282 525,300 L0,300 Z" fill="var(--card-black)"/>
      <path d="M30,236 Q190,276 440,294" fill="none" stroke="var(--brand-red)" stroke-width="3"/>
    </svg>
    <div class="wordmark">
      <span class="wordmark__dot"></span>
      <span class="wordmark__name">Wageline Associates Inc</span>
    </div>
    <div class="divider"></div>
    <div class="holder">
      <h1 class="holder__name">Marcus Hale</h1>
      <p class="holder__role">Creative Co-Operator</p>
      <address class="holder__address">4120 Cedar Hollow Lane<br>Brookvale, Utah 84321</address>
    </div>
    <ul class="contact-list">
      <li>
        <svg viewBox="0 0 12 12" aria-hidden="true"><circle cx="6" cy="6" r="6" fill="var(--brand-red)"/><path d="M4,3 L5,3 L5.6,4.6 L5,5.2 C5.4,6 6,6.6 6.8,7 L7.4,6.4 L9,7 L9,8 C9,8.5 8.5,9 8,9 C5.2,9 3,6.8 3,4 C3,3.5 3.5,3 4,3 Z" fill="#fff"/></svg>
        +000 - 555 - 019
      </li>
      <li>
        <svg viewBox="0 0 12 12" aria-hidden="true"><circle cx="6" cy="6" r="6" fill="var(--brand-red)"/><rect x="3" y="4" width="6" height="4.2" fill="none" stroke="#fff" stroke-width="0.9"/><path d="M3,4 L6,6.4 L9,4" fill="none" stroke="#fff" stroke-width="0.9"/></svg>
        hello@wagelineassoc.com
      </li>
      <li>
        <svg viewBox="0 0 12 12" aria-hidden="true"><circle cx="6" cy="6" r="6" fill="var(--brand-red)"/><circle cx="6" cy="6" r="3" fill="none" stroke="#fff" stroke-width="0.9"/><path d="M3,6 L9,6 M6,3 C4.6,5 4.6,7 6,9 M6,3 C7.4,5 7.4,7 6,9" fill="none" stroke="#fff" stroke-width="0.7"/></svg>
        www.wagelineassoc.com
      </li>
    </ul>
  </section>

  <section class="card card--back" aria-label="Business card back">
    <div class="wordmark">
      <span class="wordmark__dot"></span>
      <span class="wordmark__name">Wageline Associates Inc</span>
    </div>
    <p class="back-url">www.wagelineassoc.com</p>
  </section>
</main>
</body>
</html>
```